VELMARA Program Cover

Every year, we host an annual conference for educators who teach in afterschool in the Southwest. This year, we are renaming the conference to VELMARA 2014 (stands for Beyond-Classroom-Hours Pathways Summit). The theme of our conference is made up of three verbs: Innovate, Collaborate, & Thrive. We are looking for a program cover that is creative and yet visually appealing to an audience that ranges from Millennials to Baby Boomers. It needs to convey the three verbs and also brand the conference with the new name. We like the colors Blue and Green as our previous programs have been red, gold, yellow, and orange. Our audience teaches kids from K - 12, but likes to be treated as professionals (not the typical school clipart stuff). The conference is hosted at the Ft. Worth Calloway Lodge from July 23rd to July 24th, 2014. The program cover will set the tone for all conference materials (i.e. color scene, potential logo, etc...).

Target Market(s)

The target audience is participants of the conference. The age ranges from 25 to 60, but they are all either teachers, social workers, or educational administrators. All have a Bachelor's Degree or higher. While they are professionals, they also like to have fun.

Industry/Entity Type

Graphic Design

Requirements
Must have
• VELMARA must be prevalent and tagged with Beyond-Classroom-Hours Pathways Summit so that people know what it stands for.
Should not have
• The design should be clean with zero clipart.

```html
<!DOCTYPE html>
<html lang="en">
<head>
<meta charset="utf-8">
<title>VELMARA 2014 Program Cover</title>
<link href="https://fonts.googleapis.com/css2?family=Federo&family=Oswald:wght@600&family=Tinos&family=Open+Sans:wght@700&display=swap" rel="stylesheet">
<style>
  :root {
    --blue-deep: #1474bd;
    --blue-mid: #3f95d4;
    --blue-pale: #dcebf8;
    --blue-wave: #2f6fc0;
    --blue-wave-dark: #23489c;
    --theme-word: rgba(190, 212, 236, 0.55);
    --footer-text: #1c7cc4;
    --footer-band: #3b5ea8;
    --white: #ffffff;
  }
  * { margin: 0; padding: 0; box-sizing: border-box; }
  html, body { width: 873px; height: 1200px; overflow: hidden; background: var(--white); }
  .cover {
    position: relative;
    width: 873px;
    height: 1200px;
    overflow: hidden;
    background: linear-gradient(180deg, var(--blue-deep) 0%, var(--blue-mid) 22%, var(--blue-pale) 40%, var(--white) 52%, var(--white) 100%);
  }
  .wave-artwork {
    position: absolute;
    left: 0; top: 440px;
    width: 873px; height: 560px;
    background:
      radial-gradient(ellipse 70% 30% at 30% 62%, rgba(70,170,230,0.85), rgba(70,170,230,0) 70%),
      linear-gradient(172deg, rgba(255,255,255,0) 8%, var(--blue-wave) 30%, var(--blue-wave-dark) 48%, #4aa6e0 66%, rgba(255,255,255,0) 92%);
    -webkit-mask-image: linear-gradient(180deg, transparent 0%, #000 22%, #000 80%, transparent 100%);
    mask-image: linear-gradient(180deg, transparent 0%, #000 22%, #000 80%, transparent 100%);
  }
  .brand-name {
    position: absolute;
    left: 92px; top: 84px;
    font-family: "Federo", sans-serif;
    font-weight: 400;
    font-size: 108px;
    line-height: 1;
    color: var(--white);
    letter-spacing: -2px;
    white-space: nowrap;
  }
  .brand-year {
    position: absolute;
    left: 600px; top: 118px;
    font-family: "Federo", sans-serif;
    font-size: 96px;
    line-height: 1;
    color: var(--white);
  }
  .brand-tagline {
    position: absolute;
    left: 92px; top: 192px;
    font-family: "Oswald", sans-serif;
    font-weight: 600;
    font-size: 26px;
    line-height: 1;
    color: var(--white);
    white-space: nowrap;
  }
  .theme-word {
    position: absolute;
    font-family: "Tinos", serif;
    font-size: 92px;
    line-height: 1;
    color: var(--theme-word);
    white-space: nowrap;
  }
  .theme-innovate { left: 326px; top: 222px; }
  .theme-collaborate { left: 120px; top: 279px; }
  .theme-amp { left: 550px; top: 308px; font-size: 70px; }
  .theme-thrive { left: 473px; top: 354px; }
  .event-details {
    position: absolute;
    left: 0; top: 1060px;
    width: 873px;
    text-align: center;
    font-family: "Open Sans", sans-serif;
    font-weight: 700;
    font-size: 28px;
    line-height: 41px;
    color: var(--footer-text);
  }
  .footer-band {
    position: absolute;
    left: 0; bottom: 0;
    width: 873px; height: 36px;
    background: var(--footer-band);
  }
</style>
</head>
<body>
  <main class="cover">
    <div class="wave-artwork" role="img" aria-label="Abstract flowing blue wave ribbons with fine white line strands sweeping across the cover"></div>

    <h1 class="brand-name">VELMARA</h1>
    <div class="brand-year">2014</div>
    <p class="brand-tagline">Beyond-Classroom-Hours Pathways Summit</p>

    <div class="theme-word theme-innovate">Innovate,</div>
    <div class="theme-word theme-collaborate">Collaborate</div>
    <div class="theme-word theme-amp">&amp;</div>
    <div class="theme-word theme-thrive">Thrive</div>

    <p class="event-details">Ft. Worth Calloway Lodge<br>July 23rd to July 24th, 2014.</p>

    <div class="footer-band"></div>
  </main>
</body>
</html>
```